Brightpath Home Partners, LLC

We are private duty home care agency. We provide in-home care for people of all ages. Our kind natured and patient caregivers provide assistance to those who have difficulty with caring for themselves. We already have a logo designed by ArtMarketly

```html
<!DOCTYPE html>
<html lang="en">
<head>
<meta charset="utf-8">
<title>Brightpath Home Partners, LLC</title>
<link href="https://fonts.googleapis.com/css2?family=Poppins:wght@400;500;600;700&display=swap" rel="stylesheet">
<style>
:root{
  --orange:#f26b21;
  --green:#42a012;
  --green-dark:#2f8a0a;
  --ink:#222;
  --text:#6b6b6b;
  --light:#f0f0f0;
  --footer:#1c1c1c;
  --white:#fff;
}
*{box-sizing:border-box;margin:0;padding:0}
html,body{width:1200px;height:3797px;overflow:hidden}
body{position:relative;background:var(--white);font-family:'Poppins',sans-serif;color:var(--ink)}
.abs{position:absolute}
.photo{position:absolute;display:block}
/* top bar */
.topbar{left:0;top:0;width:1200px;height:45px;font-size:13px;color:#333}
.topbar .item{position:absolute;top:13px;display:flex;align-items:center;gap:8px}
.social{display:flex;gap:8px}
.social span{width:14px;height:14px;border:1.5px solid currentColor;border-radius:2px;display:block}
/* header */
.header{left:0;top:45px;width:1200px;height:95px}
.brand{position:absolute;left:119px;top:26px;display:flex;align-items:center;gap:10px;font-size:22px;font-weight:700;color:var(--green);line-height:1.1}
.brand i{width:18px;height:18px;background:var(--orange);border-radius:50%;display:block}
.nav{position:absolute;left:470px;top:36px;display:flex;gap:40px;font-size:14px;color:#444}
.nav .active{color:var(--orange)}
.btn-book{position:absolute;left:917px;top:28px;width:164px;height:32px;background:var(--green);color:#fff;font-size:12px;font-weight:500;display:flex;align-items:center;justify-content:center;letter-spacing:.3px}
/* hero */
.hero-photo{left:0;top:140px;width:1200px;height:560px;background:linear-gradient(90deg,#c9c3b8 0%,#ebe7e1 45%,#d7d9d6 70%,#9fb3b0 100%)}
.hero-text{left:0;top:240px;width:1200px;text-align:center}
.hero-text h1{font-size:38px;font-weight:600;color:var(--orange);line-height:50px;text-transform:uppercase}
.hero-text p{font-size:17px;color:#222;line-height:25px;margin-top:12px}
.btn-contact{display:inline-block;margin-top:30px;background:var(--orange);color:#fff;font-size:11px;padding:10px 22px;text-transform:uppercase}
.hero-dots{left:560px;top:592px;display:flex;gap:8px}
.hero-dots span{width:9px;height:9px;border-radius:50%;border:1.5px solid #fff;display:block}
.hero-dots span.on{background:#fff}
/* about */
.about{left:119px;top:760px;width:962px;height:360px;background:#fff;box-shadow:0 2px 14px rgba(0,0,0,.18)}
.about h2{position:absolute;left:40px;top:50px;font-size:26px;font-weight:600;color:var(--orange)}
.about p{position:absolute;left:40px;width:380px;font-size:12.5px;line-height:19px;color:var(--text)}
.about .about-photo{left:488px;top:8px;width:466px;height:344px;background:linear-gradient(135deg,#f1ede6,#d9d2c6 60%,#b9c2b0)}
.btn-green{position:absolute;background:var(--green);color:#fff;font-size:13px;display:flex;align-items:center;justify-content:center}
/* section titles */
.title{position:absolute;left:0;width:1200px;text-align:center;font-size:30px;font-weight:600;color:var(--orange);text-transform:uppercase}
.title b{color:var(--green);font-weight:600}
/* services */
.service{top:1261px;width:298px;height:375px;background:var(--light)}
.service .pic{left:0;top:0;width:298px;height:190px}
.service h3{position:absolute;left:24px;top:210px;width:235px;font-size:16px;font-weight:600;line-height:22px;text-transform:uppercase;color:#333}
.service p{position:absolute;left:24px;top:262px;width:250px;font-size:12px;line-height:18px;color:var(--text)}
.service .more{position:absolute;left:24px;top:332px;font-size:11px;color:var(--orange)}
.service.featured{background:var(--green)}
.service.featured h3,.service.featured p,.service.featured .more{color:#fff}
.arrow{position:absolute;top:1433px}
/* why us */
.why-text{position:absolute;top:1880px;width:520px;text-align:center;color:#fff}
.why-text h3{font-size:24px;font-weight:600;text-transform:uppercase;letter-spacing:.3px;width:400px;margin:0 auto;line-height:32px}
.why-text p{font-size:12.5px;line-height:19px;margin:14px auto 0;width:430px}
/* gallery */
.btn-view{left:535px;top:2735px;width:130px;height:38px;font-size:12px}
/* testimonial */
.quote-mark{left:0;top:2915px;width:1200px;text-align:center;font-size:46px;color:var(--green);font-weight:700;line-height:40px}
.testimonial{left:380px;top:2972px;width:440px;text-align:center;font-size:13px;line-height:22px;color:var(--text)}
.avatar{left:570px;top:3095px;width:60px;height:60px;border-radius:50%;border:3px solid #ddd;background:linear-gradient(#e7d6c6,#c4a78f)}
.author{left:0;top:3170px;width:1200px;text-align:center;font-size:12px;color:var(--green);letter-spacing:.5px}
.t-dots{left:561px;top:3210px;display:flex;gap:8px}
.t-dots span{width:11px;height:11px;border-radius:50%;border:1.5px solid #999;display:block}
.t-dots span.on{border-color:var(--orange);background:var(--orange)}
/* footer */
.footer-bg{left:0;top:3290px;width:1200px;height:507px}
.f-col{position:absolute;top:3468px;color:#fff}
.f-col h4{font-size:16px;font-weight:600;text-transform:uppercase;margin-bottom:18px}
.f-col .links a{display:block;color:#fff;font-size:12px;line-height:28px;text-decoration:none}
.f-col .line{font-size:14px;line-height:22px}
.f-col .big{font-size:22px;line-height:32px}
.f-col .big em{font-style:normal;color:var(--orange);font-weight:600}
.f-col .orange{color:var(--orange)}
.subscribe{display:flex;margin-top:4px}
.subscribe .field{width:214px;height:40px;background:#fff;color:#666;font-size:12px;padding:12px 14px}
.subscribe .go{width:68px;height:40px;background:var(--green);color:#fff;font-size:13px;display:flex;align-items:center;justify-content:center}
.copyright{left:0;top:3738px;width:1200px;text-align:center;font-size:12px;color:#ddd}
.footer-rule{left:0;top:3718px;width:1200px;height:1px;background:#3a3a3a}
</style>
</head>
<body>

<div class="abs topbar">
  <div class="item" style="left:119px">
    <svg width="11" height="16" viewBox="0 0 11 16"><rect x="1" y="1" width="9" height="14" rx="2" fill="none" stroke="#333" stroke-width="1.5"/><circle cx="5.5" cy="12.5" r="0.9" fill="#333"/></svg>
    555-010-4421
  </div>
  <div class="item" style="left:255px">
    <svg width="16" height="12" viewBox="0 0 16 12"><rect x="1" y="1" width="14" height="10" fill="none" stroke="#333" stroke-width="1.5"/><path d="M1 1l7 6 7-6" fill="none" stroke="#333" stroke-width="1.5"/></svg>
    care@brightpathhome.com
  </div>
  <div class="item social" style="left:983px;color:#333"><span></span><span></span><span></span><span></span></div>
</div>

<header class="abs header">
  <div class="brand"><i></i>Brightpath Home<br>Partners, LLC</div>
  <nav class="nav">
    <span class="active">Home</span><span>About</span><span>gallery</span><span>Services</span><span>Contact</span>
  </nav>
  <div class="btn-book">BOOK APPOINTMENT</div>
</header>

<div class="photo hero-photo" role="img" aria-label="Caregiver holding hands with a smiling senior woman in a wheelchair in a bright living room"></div>
<svg class="abs" style="left:0;top:520px" width="1200" height="180" viewBox="0 0 1200 180">
  <path d="M0 20 Q600 215 1200 20 L1200 180 L0 180 Z" fill="#42a012"/>
  <path d="M0 48 Q600 200 1200 30 L1200 180 L0 180 Z" fill="#fff"/>
</svg>
<div class="abs hero-text">
  <h1>Live Independently<br>In Your Own Home!</h1>
  <p>We provide in-home care for people of all ages<br>Call to receive FREE in-home assessment.</p>
  <div class="btn-contact">Contact Us</div>
</div>
<div class="abs hero-dots"><span></span><span class="on"></span><span></span></div>

<section class="abs about">
  <h2>ABOUT US</h2>
  <p style="top:100px">Our caregivers bring patience, warmth and steady support into every home we serve, helping each client keep the routines and comforts that matter most to them every day.</p>
  <p style="top:190px">From a few hours a week to full-time care, we shape each plan around the person, their family and the pace of life at home.</p>
  <div class="btn-green" style="left:40px;top:278px;width:142px;height:38px">Read More</div>
  <div class="photo about-photo" role="img" aria-label="Caregiver assisting a senior man seated at home"></div>
</section>

<h2 class="title" style="top:1190px">Our <b>Services</b></h2>
<svg class="arrow" style="left:48px" width="14" height="22" viewBox="0 0 14 22"><path d="M11 2 L3 11 L11 20" fill="none" stroke="#333" stroke-width="2"/></svg>
<svg class="arrow" style="left:1136px" width="14" height="22" viewBox="0 0 14 22"><path d="M3 2 L11 11 L3 20" fill="none" stroke="#333" stroke-width="2"/></svg>

<article class="abs service" style="left:119px">
  <div class="photo pic" style="background:linear-gradient(135deg,#bcd3dc,#e6e3de)" role="img" aria-label="Nurse helping a senior woman with personal care"></div>
  <h3>Help with personal hygiene and care</h3>
  <p>Gentle, respectful help with bathing, dressing and daily grooming routines.</p>
  <div class="more">Read More &rsaquo;</div>
</article>
<article class="abs service featured" style="left:453px">
  <div class="photo pic" style="background:linear-gradient(135deg,#efe9e2,#cfc6ba)" role="img" aria-label="Caregiver serving a meal to a senior woman"></div>
  <h3>Assisting with meals and nutrition</h3>
  <p>Healthy meals planned, cooked and shared to suit every diet and taste.</p>
  <div class="more">Read More &rsaquo;</div>
</article>
<article class="abs service" style="left:783px">
  <div class="photo pic" style="background:linear-gradient(135deg,#c9d7e0,#ebe6df)" role="img" aria-label="Caregiver tidying a living room while a senior rests on the sofa"></div>
  <h3>Home maintenance and housekeeping</h3>
  <p>Light cleaning, laundry and tidying so the home stays safe and calm.</p>
  <div class="more">Read More &rsaquo;</div>
</article>

<h2 class="title" style="top:1707px">Why <b>Choose Us?</b></h2>
<svg class="abs" style="left:0;top:1740px" width="1200" height="402" viewBox="0 0 1200 402" role="img" aria-label="Caregivers with seniors behind green and orange colour panels">
  <path d="M0 0 L600 80 L600 315 L0 402 Z" fill="#5fae36"/>
  <path d="M600 80 L1200 0 L1200 402 L600 315 Z" fill="#f08a55"/>
</svg>
<div class="why-text" style="left:40px">
  <h3>Companion and Personal Care</h3>
  <p>24-Hour Live-In, Overnight, Full Time, Part Time, Respite Care and More. We tailor each plan of care to the needs of the client's individual standard.</p>
</div>
<div class="why-text" style="left:648px">
  <h3>Exceptional One on One Care</h3>
  <p>Our kind natured and patient caregivers provide assistance to those who have difficulty with caring for themselves, industry's standard.</p>
</div>

<h2 class="title" style="top:2132px">Our <b>Gallery</b></h2>
<div class="photo" style="left:119px;top:2205px;width:463px;height:238px;background:linear-gradient(135deg,#e8e4dc,#c8c0b3)" role="img" aria-label="Caregiver comforting a senior man"></div>
<div class="photo" style="left:590px;top:2205px;width:238px;height:238px;background:linear-gradient(135deg,#d8dde3,#8f9fc0)" role="img" aria-label="Smiling caregiver in scrubs with a senior client"></div>
<div class="photo" style="left:836px;top:2205px;width:245px;height:238px;background:linear-gradient(135deg,#c7d7df,#e2ddd5)" role="img" aria-label="Nurse chatting with a senior woman"></div>
<div class="photo" style="left:119px;top:2451px;width:238px;height:241px;background:linear-gradient(135deg,#dfe3e6,#b9c3c9)" role="img" aria-label="Caregiver standing in a bright room with a senior on the sofa"></div>
<div class="photo" style="left:367px;top:2451px;width:243px;height:241px;background:linear-gradient(135deg,#efe8de,#d3c4b0)" role="img" aria-label="Caregiver serving juice to a senior woman"></div>
<div class="photo" style="left:618px;top:2451px;width:463px;height:241px;background:linear-gradient(135deg,#e6e4e0,#bfbab3)" role="img" aria-label="Caregiver embracing a senior woman"></div>
<div class="btn-green btn-view">VIEW ALL</div>

<h2 class="title" style="top:2844px">What our People <b>are Saying</b></h2>
<div class="abs quote-mark">&ldquo;</div>
<p class="abs testimonial">From the first visit, the caregivers treated my mother with patience and genuine kindness. They learned her routines, shared meals with her and kept our family informed every single week. Having them in the home has given all of us real peace of mind and brought back her easy smile.</p>
<div class="abs avatar" role="img" aria-label="Portrait of the reviewer"></div>
<div class="abs author">MARA ELLISON - MANAGER</div>
<div class="abs t-dots"><span class="on"></span><span></span><span></span><span></span></div>

<svg class="abs footer-bg" width="1200" height="507" viewBox="0 0 1200 507">
  <path d="M0 80 Q600 -40 1200 80 L1200 507 L0 507 Z" fill="#f26b21"/>
  <path d="M0 92 Q600 -22 1200 92 L1200 507 L0 507 Z" fill="#1c1c1c"/>
</svg>
<div class="abs footer-rule"></div>

<div class="f-col" style="left:119px">
  <h4>Quick Links</h4>
  <div class="links"><a>About Us</a><a>Services</a><a>gallery</a><a>contact</a></div>
</div>
<div class="f-col" style="left:420px;top:3456px">
  <h4>Contact Us</h4>
  <div class="big">Call. <em>555-010-4421</em></div>
  <div class="line">Fax. 555-010-7832</div>
  <div class="line">e. <span class="orange">contact@brightpathhome.com</span></div>
  <div class="big" style="margin-top:6px">ADDRESS:</div>
  <div class="line">1180 Meadowbrook Rd<br>Fairhaven Village, MI 48000</div>
</div>
<div class="f-col" style="left:762px">
  <h4>Subscribe Over Block</h4>
  <div class="subscribe"><div class="field">Enter Your Email</div><div class="go">Subscribe</div></div>
  <div class="line" style="margin-top:18px">Follow US</div>
  <div class="social" style="margin-top:14px;gap:16px;color:#fff"><span style="width:16px;height:16px"></span><span style="width:16px;height:16px"></span><span style="width:16px;height:16px"></span><span style="width:16px;height:16px"></span></div>
</div>
<div class="abs copyright">&copy; 2019 brightpathhomepartners</div>

</body>
</html>
```